Dynamic Business Card for Sports Supplements Company

Hi! I'm looking for an awesome business card to match my existing sports supplement company. I have uploaded my current company logo and screenshot of the front page of my website.

I would like to have something dynamic and interesting and utilize the colors in the website - the reds and purples

The business card should be double sided and focus on a unique eye-catching design on the back and include all the relevant company info.

Most importantly, it should say somewhere: "Sign up on our website for a coupon code."

Target Market(s)

Mostly for women gym goers but it shouldn't be too feminine. It should be in keeping with the website design. It should flow and clearly be connected to it

Industry/Entity Type

Business

Contact Information for Business Card

Lorena K. Vasquez
CEO
LVasquez@Fortivanco.example
www.fortivanco.example
614.275.3081
P.O. Box 48317
Brenton, Vermont 22417

Sign up on our website for a coupon code

Font styles to use
Serif
Sans Serif
Other font styles liked:
• Novecento font family and "Fortivan" is in AR Destine font

Requirements
Must have
• One side should be a bold Fortivan logo design. Even just the symbol itself may be o.k. (see attached file)

```html
<!DOCTYPE html>
<html lang="en">
<head>
<meta charset="utf-8">
<title>Fortivan Business Card</title>
<link rel="stylesheet" href="https://fonts.googleapis.com/css2?family=Source+Sans+3:ital,wght@0,400;0,600;0,700;1,400&display=swap">
<style>
  :root {
    --backdrop: #5b4a3b;
    --card-black: #000000;
    --brand-red: #e31b23;
    --panel-white: #ffffff;
    --ink: #1a1a1a;
    --tagline-grey: #8a8a8a;
    --text-light: #f2f2f2;
  }
  * { margin: 0; padding: 0; box-sizing: border-box; }
  html, body {
    width: 1200px; height: 987px; overflow: hidden;
    background: var(--backdrop);
    font-family: "Source Sans 3", sans-serif;
  }
  .canvas { position: relative; width: 1200px; height: 987px; }
  .card {
    position: absolute; left: 293px; width: 615px; height: 352px;
    background: var(--card-black);
    box-shadow: 0 2px 6px rgba(0,0,0,0.35);
  }
  .card--front { top: 130px; }
  .card--back { top: 505px; }

  .accent-bar {
    position: absolute; left: 0; top: 69px; width: 15px; height: 212px;
    background: var(--brand-red);
  }
  .brand-lockup {
    position: absolute; left: 56px; top: 200px; width: 215px;
    display: flex; flex-direction: column; align-items: center;
  }
  .brand-name {
    color: var(--panel-white); font-weight: 700; font-size: 36px;
    letter-spacing: 3px; text-transform: uppercase; line-height: 1;
  }
  .brand-tagline {
    color: var(--tagline-grey); font-size: 8.5px; letter-spacing: 2.4px;
    text-transform: uppercase; margin-top: 3px; white-space: nowrap;
  }
  .contact-panel {
    position: absolute; left: 316px; top: 69px; width: 299px; height: 212px;
    background: var(--panel-white); color: var(--ink);
    padding: 16px 0 0 27px; font-size: 16px; line-height: 23px;
  }
  .person-name {
    color: var(--brand-red); font-weight: 600; font-size: 22px;
    text-transform: uppercase; line-height: 25px;
  }
  .person-role { margin-bottom: 9px; }
  .address { margin-bottom: 5px; }
  .contact-line { display: flex; align-items: center; gap: 7px; }
  .contact-line svg { width: 14px; height: 14px; fill: var(--brand-red); flex: none; }

  .back-mark {
    position: absolute; left: 0; right: 0; top: 136px;
    display: flex; justify-content: center; align-items: center; gap: 14px;
  }
  .back-mark__square { width: 34px; height: 34px; background: var(--brand-red); }
  .back-mark__name {
    color: var(--panel-white); font-weight: 700; font-size: 64px;
    text-transform: uppercase; letter-spacing: 2px; line-height: 1;
  }
  .coupon-note {
    position: absolute; left: 0; right: 0; top: 290px; text-align: center;
    color: var(--text-light); font-style: italic; font-size: 16px;
  }
</style>
</head>
<body>
<main class="canvas">
  <section class="card card--front">
    <div class="accent-bar"></div>
    <div class="brand-lockup">
      <span class="brand-name">Fortivan</span>
      <span class="brand-tagline">Built For Stronger Days</span>
    </div>
    <div class="contact-panel">
      <p class="person-name">Lorena K. Vasquez</p>
      <p class="person-role">CEO</p>
      <p>P.O. Box 48317</p>
      <p class="address">Brenton, Vermont 22417</p>
      <p class="contact-line">
        <svg viewBox="0 0 24 24" aria-hidden="true"><path d="M6.6 10.8a15.1 15.1 0 0 0 6.6 6.6l2.2-2.2c.3-.3.7-.4 1-.2 1.1.4 2.3.6 3.6.6.6 0 1 .4 1 1V20c0 .6-.4 1-1 1A17 17 0 0 1 3 4c0-.6.4-1 1-1h3.5c.6 0 1 .4 1 1 0 1.3.2 2.5.6 3.6.1.3 0 .7-.2 1z"/></svg>
        614.275.3081
      </p>
      <p class="contact-line">
        <svg viewBox="0 0 24 24" aria-hidden="true"><path d="M2 5h20v14H2z M2 5l10 8 10-8" stroke="#fff" stroke-width="1.5"/></svg>
        LVasquez@Fortivanco.example
      </p>
      <p class="contact-line">
        <svg viewBox="0 0 24 24" aria-hidden="true"><circle cx="12" cy="12" r="10"/><path d="M8 6c2 1 1 3 3 4s1 3-1 4M15 14c1 1 2 2 1 4" stroke="#fff" stroke-width="1.6" fill="none"/></svg>
        www.fortivanco.example
      </p>
    </div>
  </section>

  <section class="card card--back">
    <div class="back-mark">
      <span class="back-mark__square"></span>
      <span class="back-mark__name">Fortivan</span>
    </div>
    <p class="coupon-note">Sign up on our website for a coupon code</p>
  </section>
</main>
</body>
</html>
```